Disposable Mini Sauce Pot Design for Asian Chain Food Brands

We operate a Hainan Chicken Rice takeout brand under the name Wokly8, with our official website: www.Wokly8.com.
We offer four signature house sauces and are launching brand-new packaging for our sauce line. We require custom graphic designs exclusively for the sauce cup lids.
Product Material & Base Specs
The sauce cups are made of PP plastic, available in two translucent base options: Translucent White and Translucent Orange.
Four Sauce Varieties for Individual Lid Designs
1. Red Sauce – Fried Sweet Chili Sauce
2.Green Sauce – Scallion Oil Dressing
3.Sweet Soy Sauce
4.Sweet Red Sauce (Special for Fried Chicken)
Differentiate each sauce lid design through unique graphics, typography, or illustrative elements for easy customer identification.
The marking NET WT 2 OZ must be clearly printed on every lid.
**There is no need to print full descriptive text or the full name of the sauces on each lid; the design only needs to clearly differentiate the four sauce varieties.
**Please reference the original design style and brand color palette shown on our official website, and feel free to fully unleash your creativity.
Look and feel
Each slider illustrates characteristics of the customer's brand and the style your logo design should communicate.

```html
<!DOCTYPE html>
<html lang="en">
<head>
<meta charset="utf-8">
<title>Wokly8 Sauce Lid Set</title>
<link rel="stylesheet" href="https://fonts.googleapis.com/css2?family=Montserrat:wght@800;900&display=swap">
<style>
  :root {
    --page: #ffffff;
    --ink: #ffffff;
    --band: #8a0b22;
    --red: #e30613;
    --red-deep: #d0120f;
    --green: #6cae2c;
    --green-deep: #62a527;
    --orange: #ec7322;
    --orange-deep: #e2661c;
    --pink: #e63e6b;
    --pink-deep: #dc3462;
  }
  html, body {
    margin: 0;
    padding: 0;
    width: 1072px;
    height: 1200px;
    overflow: hidden;
    background: var(--page);
  }
  .lid-sheet {
    position: relative;
    width: 1072px;
    height: 1200px;
  }
  .lid {
    position: absolute;
    width: 471px;
    height: 533px;
    display: block;
  }
  .lid--red { left: 62px; top: 70px; }
  .lid--green { left: 555px; top: 70px; }
  .lid--soy { left: 62px; top: 626px; }
  .lid--sweet-red { left: 555px; top: 626px; }
  .headline {
    font-family: "Montserrat", sans-serif;
    font-weight: 900;
    fill: var(--ink);
  }
  .band { fill: var(--band); }
  .band-text {
    font-family: "Montserrat", sans-serif;
    font-weight: 900;
    fill: var(--ink);
  }
  .net-weight { font-size: 27px; }
  .variety { font-size: 36px; text-anchor: middle; }
  .brand { font-size: 40px; text-anchor: middle; }
</style>
</head>
<body>
<main class="lid-sheet">

  <svg class="lid lid--red" viewBox="0 0 795 900" aria-label="Red sauce lid">
    <defs>
      <clipPath id="lid-shape-a"><path d="M100,0 H695 A100,100 0 0 1 795,100 V770 A130,130 0 0 1 665,900 H130 A130,130 0 0 1 0,770 V100 A100,100 0 0 1 100,0 Z"/></clipPath>
      <radialGradient id="glow-red" cx="0.5" cy="0.45" r="0.7"><stop offset="0" stop-color="var(--red)"/><stop offset="1" stop-color="var(--red-deep)"/></radialGradient>
    </defs>
    <g clip-path="url(#lid-shape-a)">
      <rect width="795" height="900" fill="url(#glow-red)"/>
      <path class="band" d="M0,768 Q85,745 175,758 T345,774 Q425,746 505,756 T680,770 Q745,752 795,748 V900 H0 Z"/>
    </g>
    <text class="headline" x="94" y="570" font-size="665" textLength="416" lengthAdjust="spacingAndGlyphs">R</text>
    <text class="headline" x="522" y="335" font-size="318" textLength="170" lengthAdjust="spacingAndGlyphs">E</text>
    <text class="headline" x="522" y="575" font-size="318" textLength="223" lengthAdjust="spacingAndGlyphs">D</text>
    <text class="headline" x="78" y="707" font-size="208" textLength="649" lengthAdjust="spacingAndGlyphs">sauce</text>
    <text class="band-text net-weight" x="35" y="828">NET WT 2 OZ</text>
    <text class="band-text variety" x="397" y="835">FRIED SWEET</text>
    <text class="band-text variety" x="397" y="868">CHILI SAUCE</text>
    <text class="band-text brand" x="675" y="834">Wokly8</text>
  </svg>

  <svg class="lid lid--green" viewBox="0 0 795 900" aria-label="Green sauce lid">
    <defs>
      <clipPath id="lid-shape-b"><path d="M100,0 H695 A100,100 0 0 1 795,100 V770 A130,130 0 0 1 665,900 H130 A130,130 0 0 1 0,770 V100 A100,100 0 0 1 100,0 Z"/></clipPath>
      <radialGradient id="glow-green" cx="0.5" cy="0.45" r="0.7"><stop offset="0" stop-color="var(--green)"/><stop offset="1" stop-color="var(--green-deep)"/></radialGradient>
    </defs>
    <g clip-path="url(#lid-shape-b)">
      <rect width="795" height="900" fill="url(#glow-green)"/>
      <path class="band" d="M0,760 Q85,748 175,764 T345,770 Q425,748 505,760 T680,768 Q745,752 795,748 V900 H0 Z"/>
    </g>
    <text class="headline" x="108" y="386" font-size="410" textLength="582" lengthAdjust="spacingAndGlyphs">GR</text>
    <text class="headline" x="125" y="604" font-size="298" textLength="566" lengthAdjust="spacingAndGlyphs">EEN</text>
    <text class="headline" x="123" y="722" font-size="185" textLength="568" lengthAdjust="spacingAndGlyphs">sauce</text>
    <text class="band-text net-weight" x="35" y="828">NET WT 2 OZ</text>
    <text class="band-text variety" x="397" y="835">SCALLION OIL</text>
    <text class="band-text variety" x="397" y="868">DRESSING</text>
    <text class="band-text brand" x="675" y="834">Wokly8</text>
  </svg>

  <svg class="lid lid--soy" viewBox="0 0 795 900" aria-label="Sweet soy sauce lid">
    <defs>
      <clipPath id="lid-shape-c"><path d="M100,0 H695 A100,100 0 0 1 795,100 V770 A130,130 0 0 1 665,900 H130 A130,130 0 0 1 0,770 V100 A100,100 0 0 1 100,0 Z"/></clipPath>
      <radialGradient id="glow-orange" cx="0.5" cy="0.45" r="0.7"><stop offset="0" stop-color="var(--orange)"/><stop offset="1" stop-color="var(--orange-deep)"/></radialGradient>
    </defs>
    <g clip-path="url(#lid-shape-c)">
      <rect width="795" height="900" fill="url(#glow-orange)"/>
      <path class="band" d="M0,770 Q85,748 175,760 T345,778 Q425,750 505,756 T680,760 Q745,748 795,746 V900 H0 Z"/>
    </g>
    <text class="headline" x="123" y="272" font-size="295" textLength="552" lengthAdjust="spacingAndGlyphs">SW</text>
    <text class="headline" x="120" y="482" font-size="335" textLength="540" lengthAdjust="spacingAndGlyphs">eet</text>
    <text class="headline" x="127" y="672" font-size="250" textLength="533" lengthAdjust="spacingAndGlyphs">SOY</text>
    <text class="headline" x="265" y="738" font-size="86" textLength="265" lengthAdjust="spacingAndGlyphs">sauce</text>
    <text class="band-text net-weight" x="35" y="830">NET WT 2 OZ</text>
    <text class="band-text brand" x="675" y="834">Wokly8</text>
  </svg>

  <svg class="lid lid--sweet-red" viewBox="0 0 795 900" aria-label="Sweet red sauce lid">
    <defs>
      <clipPath id="lid-shape-d"><path d="M100,0 H695 A100,100 0 0 1 795,100 V770 A130,130 0 0 1 665,900 H130 A130,130 0 0 1 0,770 V100 A100,100 0 0 1 100,0 Z"/></clipPath>
      <radialGradient id="glow-pink" cx="0.5" cy="0.45" r="0.7"><stop offset="0" stop-color="var(--pink)"/><stop offset="1" stop-color="var(--pink-deep)"/></radialGradient>
    </defs>
    <g clip-path="url(#lid-shape-d)">
      <rect width="795" height="900" fill="url(#glow-pink)"/>
      <path class="band" d="M0,762 Q85,748 175,762 T345,780 Q425,750 505,758 T680,760 Q745,748 795,746 V900 H0 Z"/>
    </g>
    <text class="headline" x="123" y="272" font-size="295" textLength="552" lengthAdjust="spacingAndGlyphs">SW</text>
    <text class="headline" x="120" y="482" font-size="335" textLength="540" lengthAdjust="spacingAndGlyphs">eet</text>
    <text class="headline" x="146" y="672" font-size="250" textLength="522" lengthAdjust="spacingAndGlyphs">RED</text>
    <text class="headline" x="266" y="738" font-size="86" textLength="264" lengthAdjust="spacingAndGlyphs">sauce</text>
    <text class="band-text net-weight" x="35" y="830">NET WT 2 OZ</text>
    <text class="band-text variety" x="397" y="834">SPECIAL FOR</text>
    <text class="band-text variety" x="397" y="869">FRIED CHICKEN</text>
    <text class="band-text brand" x="675" y="834">Wokly8</text>
  </svg>

</main>
</body>
</html>
```